Banner Ad in Spanish for Car Accident Law Firm in Miami Florida

I need a Banner Ad in Spanish Language. We are an Accident Law Firm in Miami, FL. We help injured people. I need a Banner Ad with a Vibrant Colorful Background to Stand Out. A Click-Able Call to Action is needed. We don't want to make the banner too crowded and we want the message to be simple to understand. We are looking for a skilled graphic designer to create a visually appealing banner ad for our YouTube marketing campaign. The required dimensions and format are:
1920 x 275
.png & .mp4

The Banner is for our Plaintiff’s Personal Injury Law Firm. We represent Spanish Speaking clients who are injured in CAR ACCIDENTS. As such the banner must include:
1. Our Firm Logo
2. Our Telephone# (305) 471-6203
3. Stock Photo of Car Crash
4. Photo of our attorney in office
5. The Words Abogados de Accidentes
The telephone number should be fairly large and stand out it is our call to action. The words Abogados de Accidentes should be close to our Logo to associate the two.

Target Market(s)

Car Accident Victims who speak Spanish

Industry/Entity Type

Legal, Law Firm.

Font styles to use
Sans Serif

Colors
59FF00
82FF00
B8FF75
E3FFCB
F4FFEA
F0912C
F2A743
F7CA91
FBE8D2
FDF5EE
6B429C
8869AF
B7A5CE
E3DAEB
F3F0F8

Requirements
Must have
• A bold background so that Banner Ad can be seen on mobile and against the screen being advertising against
Should not have
• Be too crowded. Hard to understand what it is for.

```html
<!DOCTYPE html>
<html lang="es">
<head>
<meta charset="utf-8">
<title>Abogados de Accidentes – Banners</title>
<link rel="stylesheet" href="https://fonts.googleapis.com/css2?family=Fira+Sans:wght@500;600;700&display=swap">
<style>
  :root {
    --navy: #2a2a72;
    --navy-deep: #1f1f5c;
    --navy-stripe: #34348a;
    --yellow: #f6b63a;
    --white: #ffffff;
    --label: #1f2150;
    --foliage: #4d6b34;
    --silver: #a7aeb8;
    --steel: #6c7582;
    --asphalt: #1b1f2c;
    --suit-light: #9a9ca2;
    --suit-mid: #6d7078;
    --suit-dark: #3a3d45;
    --skin: #c9a08a;
  }
  html, body {
    margin: 0;
    padding: 0;
    width: 763px;
    height: 1200px;
    overflow: hidden;
    background: var(--white);
    font-family: "Fira Sans", Arial, sans-serif;
  }
  .sheet { position: relative; width: 763px; height: 1200px; }
  .format { position: absolute; left: 51px; width: 661px; display: block; }
  .format--full { top: 48px; height: 372px; }
  .format--strip-blank { top: 479px; height: 94px; }
  .format--full-ad { top: 645px; height: 372px; }
  .format--strip-ad { top: 1054px; height: 94px; }
  .size-label {
    position: absolute; left: 0; width: 763px; text-align: center;
    font-size: 13px; font-weight: 600; color: var(--label); margin: 0;
    letter-spacing: 0.3px;
  }
  .size-label--full { top: 434px; }
  .size-label--strip { top: 587px; }
  .brand { font-weight: 600; fill: var(--navy); }
  .headline { font-weight: 700; fill: var(--white); }
  .phone-text { font-weight: 700; fill: var(--navy-deep); }
</style>
</head>
<body>
<main class="sheet">

  <svg class="format format--full" viewBox="0 0 661 372" aria-label="Lienzo 1920x1080">
    <rect width="661" height="372" fill="var(--navy)"/>
  </svg>
  <p class="size-label size-label--full">1920x1080</p>

  <svg class="format format--strip-blank" viewBox="0 0 661 94" aria-label="Lienzo 1920x275">
    <rect width="661" height="94" fill="var(--navy)"/>
  </svg>
  <p class="size-label size-label--strip">1920x275</p>

  <svg width="0" height="0" style="position:absolute">
    <defs>
      <linearGradient id="car-tone" x1="0" y1="0" x2="0.6" y2="1">
        <stop offset="0" stop-color="var(--foliage)"/>
        <stop offset="0.3" stop-color="var(--silver)"/>
        <stop offset="0.6" stop-color="var(--steel)"/>
        <stop offset="1" stop-color="var(--asphalt)"/>
      </linearGradient>
      <radialGradient id="car-glow" cx="0.75" cy="0.35" r="0.5">
        <stop offset="0" stop-color="#c9cfd6" stop-opacity="0.7"/>
        <stop offset="1" stop-color="#c9cfd6" stop-opacity="0"/>
      </radialGradient>
      <linearGradient id="person-tone" x1="0" y1="0" x2="0" y2="1">
        <stop offset="0" stop-color="var(--skin)"/>
        <stop offset="0.22" stop-color="var(--skin)" stop-opacity="0.9"/>
        <stop offset="0.3" stop-color="var(--suit-light)"/>
        <stop offset="0.7" stop-color="var(--suit-mid)"/>
        <stop offset="1" stop-color="var(--suit-dark)"/>
      </linearGradient>
    </defs>
  </svg>

  <!-- Full-size ad -->
  <svg class="format format--full-ad" viewBox="0 0 661 372">
    <rect class="ad-bg" width="661" height="372" fill="var(--navy)"/>
    <g class="ad-stripes" fill="var(--navy-stripe)" opacity="0.85">
      <polygon points="0,120 40,95 230,372 160,372 0,170"/>
      <polygon points="0,240 0,290 70,372 125,372"/>
    </g>
    <g class="car-photo" role="img" aria-label="Foto de choque de autos">
      <polygon points="603,0 661,0 661,372 312,372" fill="url(#car-tone)"/>
      <polygon points="603,0 661,0 661,372 312,372" fill="url(#car-glow)"/>
    </g>
    <polygon class="logo-plate" points="0,17 196,17 152,79 0,79" fill="var(--white)"/>
    <rect class="logo-mark" x="26" y="34" width="24" height="24" fill="var(--navy)"/>
    <text class="brand" x="56" y="52" font-size="17">MORAVEC</text>
    <text class="brand" x="89" y="63" font-size="7">LAW FIRM</text>
    <path class="attorney-photo" role="img" aria-label="Foto del abogado en traje"
          d="M78,102 q38,0 38,38 l0,40 q38,10 40,50 l0,142 l-120,0 l0,-140 q4,-42 40,-52 l0,-40 q0,-38 2,-38z"
          fill="url(#person-tone)"/>
    <text class="headline" x="178" y="127" font-size="36">Abogados de</text>
    <text class="headline" x="178" y="174" font-size="36">Accidentes</text>
    <rect class="divider" x="178" y="191" width="28" height="3" fill="var(--white)"/>
    <text class="headline" x="178" y="235" font-size="31">Consulta Gratis</text>
    <rect class="cta-pill" x="210" y="276" width="250" height="39" rx="10" fill="var(--yellow)"/>
    <circle class="cta-icon" cx="201" cy="295" r="24" fill="var(--navy)" stroke="var(--yellow)" stroke-width="3"/>
    <path class="phone-glyph" d="M193,285 c2,-1 4,0 5,2 l2,4 c0,2 -1,3 -2,4 c1,3 4,6 7,7 c1,-1 2,-2 4,-2 l4,2 c2,1 3,3 2,5 c-1,2 -3,3 -5,3 c-10,-1 -19,-10 -20,-20 c0,-2 1,-4 3,-5z" fill="var(--yellow)"/>
    <text class="phone-text" x="237" y="305" font-size="27">(305) 471-6203</text>
  </svg>

  <!-- Strip ad -->
  <svg class="format format--strip-ad" viewBox="0 0 661 94">
    <polygon class="ad-bg" points="102,0 661,0 661,94 132,94" fill="var(--navy)"/>
    <polygon class="ad-stripes" points="200,0 235,0 305,94 270,94" fill="var(--navy-stripe)" opacity="0.85"/>
    <g class="car-photo" role="img" aria-label="Foto de choque de autos">
      <polygon points="539,0 661,0 661,94 483,94" fill="url(#car-tone)"/>
      <polygon points="539,0 661,0 661,94 483,94" fill="url(#car-glow)"/>
    </g>
    <rect class="logo-mark" x="15" y="35" width="19" height="19" fill="var(--navy)"/>
    <text class="brand" x="38" y="48" font-size="13">MORAVEC</text>
    <text class="brand" x="65" y="56" font-size="5.5">LAW FIRM</text>
    <path class="attorney-photo" role="img" aria-label="Foto del abogado en traje"
          d="M162,9 q14,0 14,16 l0,10 q16,5 17,22 l0,37 l-61,0 l0,-37 q2,-17 17,-22 l0,-10 q0,-16 13,-16z"
          fill="url(#person-tone)"/>
    <text class="headline" x="327" y="25" font-size="19" text-anchor="middle">Abogados de Accidentes</text>
    <text class="headline" x="327" y="51" font-size="19" text-anchor="middle">Consulta Gratis</text>
    <rect class="cta-pill" x="272" y="64" width="134" height="20" rx="5" fill="var(--yellow)"/>
    <circle class="cta-icon" cx="267" cy="74" r="12" fill="var(--navy)" stroke="var(--yellow)" stroke-width="2"/>
    <path class="phone-glyph" d="M263,69 c1,-0.5 2,0 2.5,1 l1,2 c0,1 -0.5,1.5 -1,2 c0.5,1.5 2,3 3.5,3.5 c0.5,-0.5 1,-1 2,-1 l2,1 c1,0.5 1.5,1.5 1,2.5 c-0.5,1 -1.5,1.5 -2.5,1.5 c-5,-0.5 -9.5,-5 -10,-10 c0,-1 0.5,-2 1.5,-2.5z" fill="var(--yellow)"/>
    <text class="phone-text" x="286" y="79" font-size="14">(305) 471-6203</text>
  </svg>

</main>
</body>
</html>
```